Business card for IT company

Looking for a business card for an IT company providing server, network, and application support to medium businesses. Company name is Calderwick Systems. Website is www.calderwicksystems.example, would like to use the green color that is on the homepage. Prefer design to be done in Illustrator. Please, only DESIGNERS apply - no PHP programmers attempting to do design. Thank you

Industry/Entity Type

Information Technology

Requirements
Must have
• Green
Should not have
• Template designs, or designs done by non-designer type people

```html
<!DOCTYPE html>
<html lang="en">
<head>
<meta charset="utf-8">
<title>Calderwick Systems — Business Card</title>
<link href="https://fonts.googleapis.com/css2?family=Raleway:wght@300;400&display=swap" rel="stylesheet">
<style>
  :root {
    --page: #e9e4dc;
    --green-light: #c2e25c;
    --green: #9fcf3f;
    --green-deep: #7fb52c;
    --tile-green: #9ccc45;
    --tile-yellow: #e0d021;
    --tile-blue: #12a8d8;
    --tile-orange: #e7a834;
    --tile-purple: #c270d8;
    --white: #ffffff;
    --card-edge: #f4f4f4;
  }
  * { box-sizing: border-box; margin: 0; padding: 0; }
  html, body {
    width: 1200px; height: 1023px; overflow: hidden;
    background: var(--page);
    font-family: "Raleway", sans-serif;
  }
  .sheet {
    position: relative; width: 1200px; height: 1023px;
    display: flex; flex-direction: column; align-items: center; justify-content: center; gap: 70px;
  }
  .card {
    width: 640px; height: 366px; border-radius: 22px; overflow: hidden;
    box-shadow: 0 10px 28px rgba(60, 45, 25, 0.22);
  }
  /* Front */
  .card--front {
    background: radial-gradient(ellipse at 60% 35%, var(--green-light) 0%, var(--green) 55%, var(--green-deep) 100%);
    display: flex; align-items: center; justify-content: center; gap: 26px;
  }
  .brand-mark {
    width: 112px; height: 112px; border-radius: 50%; background: var(--white); flex: none;
  }
  .brand-name {
    color: var(--white); font-weight: 300; line-height: 1;
    display: flex; flex-direction: column; align-items: flex-end; gap: 8px;
  }
  .brand-name__main { font-size: 50px; letter-spacing: 1px; }
  .brand-name__sub { font-size: 24px; letter-spacing: 2px; }
  /* Back */
  .card--back {
    background: var(--card-edge); padding: 9px;
    display: grid; grid-template-columns: repeat(3, 1fr); grid-template-rows: 1fr 1fr; gap: 8px;
  }
  .tile {
    border-radius: 4px; color: var(--white); position: relative;
    display: flex; flex-direction: column; align-items: center; justify-content: center; gap: 14px;
  }
  .tile--logo { background: var(--tile-green); flex-direction: row; gap: 12px; }
  .tile--name { background: var(--tile-yellow); grid-column: span 2; align-items: flex-start; padding-left: 36px; }
  .tile--email { background: var(--tile-blue); }
  .tile--phone { background: var(--tile-orange); }
  .tile--web { background: var(--tile-purple); }
  .tile-mark { width: 46px; height: 46px; border-radius: 50%; background: var(--white); flex: none; }
  .tile-brand { font-weight: 300; line-height: 1.05; display: flex; flex-direction: column; align-items: flex-end; }
  .tile-brand__main { font-size: 21px; }
  .tile-brand__sub { font-size: 11px; letter-spacing: 1.5px; }
  .person-name { font-size: 36px; font-weight: 400; letter-spacing: 1px; }
  .person-title { font-size: 14px; font-weight: 400; margin-top: -8px; }
  .person-icon { position: absolute; right: 28px; bottom: 18px; }
  .contact-text { font-size: 11.5px; font-weight: 400; text-align: center; padding: 0 6px; }
  .contact-text--phone { font-size: 14px; letter-spacing: 2px; }
</style>
</head>
<body>
<main class="sheet">
  <section class="card card--front" aria-label="Card front">
    <span class="brand-mark"></span>
    <h1 class="brand-name">
      <span class="brand-name__main">CALDERWICK</span>
      <span class="brand-name__sub">SYSTEMS</span>
    </h1>
  </section>

  <section class="card card--back" aria-label="Card back">
    <div class="tile tile--logo">
      <span class="tile-mark"></span>
      <span class="tile-brand">
        <span class="tile-brand__main">CALDERWICK</span>
        <span class="tile-brand__sub">SYSTEMS</span>
      </span>
    </div>
    <div class="tile tile--name">
      <p class="person-name">Your Name</p>
      <p class="person-title">Title</p>
      <svg class="person-icon" width="86" height="72" viewBox="0 0 86 72" fill="none" stroke="#fff" stroke-width="2.5" stroke-linecap="round">
        <circle cx="56" cy="20" r="17"/>
        <path d="M4 38 C20 26 34 30 40 40 C46 52 40 64 28 70"/>
      </svg>
    </div>
    <div class="tile tile--email">
      <svg width="78" height="54" viewBox="0 0 78 54" fill="none" stroke="#fff" stroke-width="2.5" stroke-linejoin="round">
        <rect x="2" y="2" width="74" height="50"/>
        <path d="M2 2 L39 32 L76 2 M2 52 L30 25 M76 52 L48 25"/>
      </svg>
      <p class="contact-text">support@calderwicksystems.example</p>
    </div>
    <div class="tile tile--phone">
      <svg width="44" height="44" viewBox="0 0 44 44" fill="#fff">
        <path d="M10 4 C6 5 3 9 4 14 C7 27 17 37 30 40 C35 41 39 38 40 34 L33 27 L27 30 C21 27 17 23 14 17 L17 11 Z"/>
      </svg>
      <p class="contact-text contact-text--phone">555.014.2286</p>
    </div>
    <div class="tile tile--web">
      <svg width="52" height="52" viewBox="0 0 52 52" fill="none" stroke="#fff" stroke-width="2.5" stroke-linejoin="round">
        <path d="M6 6 L46 20 L30 26 L44 40 L38 46 L24 32 L18 48 Z"/>
      </svg>
      <p class="contact-text">www.calderwicksystems.example</p>
    </div>
  </section>
</main>
</body>
</html>
```